Business card for massage therapy company called Brook Fern Wellness

Need business card for massage therapy company called Brook Fern Wellness. Would like my logo on the front and the back of the card I have 3 options of logos and you can play with what looks better.

Would like this information displayed on the back of the card:

Marcus Ellery
Licensed Massage Therapist
321-555-0147
brookfern-example.com
brookfern_rest_

```html
<!DOCTYPE html>
<html lang="en">
<head>
<meta charset="utf-8">
<title>Brook Fern Wellness – Business Card</title>
<link rel="stylesheet" href="https://fonts.googleapis.com/css2?family=Jost:wght@300;400&display=swap">
<style>
  :root {
    --page-bg: #e8e3dd;
    --card-bg: #eeebe6;
    --panel-sage: #8c978b;
    --panel-copper: #b88a72;
    --ink-name: #59594a;
    --ink-title: #a67c66;
    --ink-contact: #5e5b54;
    --ink-icon: #9b7a68;
    --logo-ink: #ffffff;
  }
  html, body {
    margin: 0;
    padding: 0;
    width: 1200px;
    height: 1054px;
    overflow: hidden;
    background: var(--page-bg);
  }
  .business-card {
    position: absolute;
    left: 100px;
    top: 241px;
    width: 1000px;
    height: 572px;
    border-radius: 28px;
    background: var(--card-bg);
    overflow: hidden;
    box-shadow: 0 2px 10px rgba(0,0,0,0.08);
    font-family: "Jost", sans-serif;
  }
  .brand-panel {
    position: absolute;
    left: 0;
    top: 0;
    width: 1000px;
    height: 572px;
  }
  .brand-mark {
    position: absolute;
    left: 0;
    top: 0;
    width: 420px;
    text-align: center;
    color: var(--logo-ink);
    font-weight: 300;
  }
  .brand-ring {
    position: absolute;
    left: 136px;
    top: 158px;
    width: 148px;
    height: 148px;
    border: 2px solid var(--logo-ink);
    border-radius: 50%;
    box-sizing: border-box;
  }
  .brand-name {
    position: absolute;
    left: 0;
    top: 318px;
    width: 420px;
    font-size: 46px;
    letter-spacing: 3px;
    line-height: 1;
    margin: 0;
  }
  .brand-sub {
    position: absolute;
    left: 0;
    top: 384px;
    width: 420px;
    font-size: 28px;
    letter-spacing: 7px;
    line-height: 1;
    margin: 0;
  }
  .person {
    position: absolute;
    right: 75px;
    top: 130px;
    text-align: right;
  }
  .person-name {
    margin: 0;
    font-size: 46px;
    font-weight: 400;
    color: var(--ink-name);
    line-height: 1;
  }
  .person-title {
    margin: 14px 0 0;
    font-size: 24px;
    font-weight: 300;
    color: var(--ink-title);
    line-height: 1;
  }
  .contact-list {
    position: absolute;
    right: 76px;
    top: 312px;
    margin: 0;
    padding: 0;
    list-style: none;
    text-align: right;
  }
  .contact-item {
    display: flex;
    justify-content: flex-end;
    align-items: center;
    gap: 14px;
    height: 41px;
    font-size: 23px;
    font-weight: 300;
    color: var(--ink-contact);
  }
  .contact-item.social { flex-direction: row-reverse; }
  .contact-icon {
    width: 22px;
    height: 22px;
    flex: none;
  }
  .social-dot {
    width: 22px;
    height: 22px;
    border-radius: 50%;
    background: var(--ink-icon);
    flex: none;
  }
</style>
</head>
<body>
  <div class="business-card">
    <svg class="brand-panel" viewBox="0 0 1000 572" aria-hidden="true">
      <path d="M0,0 H436 Q556,286 436,572 H0 Z" fill="var(--panel-copper)"/>
      <path d="M0,0 H420 Q540,286 420,572 H0 Z" fill="var(--panel-sage)"/>
    </svg>

    <div class="brand-mark">
      <div class="brand-ring"></div>
      <p class="brand-name">BROOK FERN</p>
      <p class="brand-sub">WELLNESS</p>
    </div>

    <div class="person">
      <h1 class="person-name">Marcus Ellery</h1>
      <p class="person-title">Licensed Massage Therapist</p>
    </div>

    <ul class="contact-list">
      <li class="contact-item social">
        <span>brookfern_rest</span>
        <span class="social-dot"></span>
      </li>
      <li class="contact-item">
        <span>321-555-0147</span>
        <svg class="contact-icon" viewBox="0 0 24 24" aria-hidden="true">
          <path d="M3 9 Q12 3 21 9 L19 12 L16 10.5 L16 8.5 Q12 7 8 8.5 L8 10.5 L5 12 Z" fill="var(--ink-icon)"/>
          <path d="M6 20 L7.5 12.5 H16.5 L18 20 Z" fill="var(--ink-icon)"/>
        </svg>
      </li>
      <li class="contact-item">
        <span>marcus@brookfern-example.com</span>
        <svg class="contact-icon" viewBox="0 0 24 24" aria-hidden="true">
          <rect x="2" y="5" width="20" height="14" fill="var(--ink-icon)"/>
          <path d="M2 5 L12 13 L22 5" fill="none" stroke="var(--card-bg)" stroke-width="1.6"/>
        </svg>
      </li>
      <li class="contact-item">
        <span>www.brookfern-example.com</span>
        <svg class="contact-icon" viewBox="0 0 24 24" aria-hidden="true">
          <circle cx="12" cy="12" r="9" fill="var(--ink-icon)"/>
          <g fill="none" stroke="var(--card-bg)" stroke-width="1.2">
            <ellipse cx="12" cy="12" rx="4" ry="9"/>
            <line x1="3" y1="12" x2="21" y2="12"/>
            <line x1="12" y1="3" x2="12" y2="21"/>
          </g>
        </svg>
      </li>
    </ul>
  </div>
</body>
</html>
```